Wine label Design

We are looking to develop an elegant contemporary Chilean design; for a new Wine Brand ZORIVEN to be sold in Chinese Market.
We would like to see designs that are a fine balance between having a traditional design that can offer quality reassurance and being distinctive enough to stand out on crowded shelves. The final design should be easy-to-remember and communicate Quality, Tradition and have a conection with Chile.

Target Market(s)

Urban Chinese between 25 to 40 yo

Requirements
Must have
• Paper label
Information on Front label : Grape (example Cabernet sauvignon) / Vintage (ex 2010) / Wine of Chile
Bottle shape is given (see attached)
Nice to have
• An element of uniqueness, easy to recall the brand
Red and Gold Color are appreciated by the Target
Should not have
• White background
Number 4 is considered death, should not be included on the design

```html
<!DOCTYPE html>
<html lang="en">
<head>
<meta charset="utf-8">
<title>ZORIVEN – Wine Label</title>
<link rel="stylesheet" href="https://fonts.googleapis.com/css2?family=Josefin+Sans:wght@300;400&display=swap">
<style>
  :root {
    --page-bg: #ffffff;
    --label-paper: #eef1f0;
    --wine-red: #8a1f2c;
    --ink-dark: #2a2a2a;
    --gold-light: #f6e6b8;
    --gold-mid: #c99a4b;
    --gold-deep: #9a5b1e;
    --art-tone: #e7d8d9;
  }
  html, body {
    margin: 0;
    padding: 0;
    width: 1200px;
    height: 900px;
    overflow: hidden;
    background: var(--page-bg);
  }
  .canvas {
    position: relative;
    width: 1200px;
    height: 900px;
    font-family: "Josefin Sans", "Century Gothic", sans-serif;
  }
  .label-shape {
    position: absolute;
    left: 350px;
    top: 30px;
    width: 500px;
    height: 840px;
  }
  .brand-name {
    position: absolute;
    left: 350px;
    width: 500px;
    top: 232px;
    margin: 0;
    text-align: center;
    font-weight: 300;
    font-size: 70px;
    letter-spacing: 2px;
    color: var(--wine-red);
    line-height: 1;
  }
  .brand-divider {
    position: absolute;
    left: 468px;
    top: 318px;
    width: 264px;
    height: 24px;
  }
  .brand-divider .rule {
    position: absolute;
    top: 11px;
    height: 1.5px;
    width: 94px;
    background: var(--wine-red);
  }
  .brand-divider .rule--left { left: 0; }
  .brand-divider .rule--right { right: 0; }
  .brand-divider .flourish {
    position: absolute;
    left: 100px;
    top: 4px;
    width: 64px;
    height: 16px;
    background: linear-gradient(90deg, #c58a92, var(--wine-red), #c58a92);
    border-radius: 8px;
  }
  .wine-details {
    position: absolute;
    right: 407px;
    top: 420px;
    text-align: right;
    color: var(--ink-dark);
  }
  .grape {
    margin: 0;
    font-weight: 300;
    font-size: 31px;
    line-height: 1;
  }
  .vintage {
    margin: 10px 0 0;
    font-weight: 300;
    font-size: 24px;
    letter-spacing: 5px;
    line-height: 1;
  }
  .origin {
    margin: 32px 0 0;
    font-weight: 300;
    font-size: 23px;
    letter-spacing: 0.5px;
    color: var(--wine-red);
    line-height: 1;
  }
  .art-area {
    position: absolute;
    left: 380px;
    top: 530px;
    width: 156px;
    height: 280px;
    border-radius: 30px 40px 10px 10px;
    background: linear-gradient(160deg, var(--art-tone), #f1e7e8);
  }
</style>
</head>
<body>
  <main class="canvas">
    <svg class="label-shape" viewBox="0 0 500 840" aria-hidden="true">
      <defs>
        <linearGradient id="gold-band" x1="0" y1="0" x2="1" y2="0">
          <stop offset="0" stop-color="#9a5b1e"/>
          <stop offset="0.35" stop-color="#f6e6b8"/>
          <stop offset="0.65" stop-color="#c99a4b"/>
          <stop offset="1" stop-color="#9a5b1e"/>
        </linearGradient>
      </defs>
      <path class="label-gold" fill="url(#gold-band)"
            d="M0,170 Q250,-10 500,150 L500,620 Q360,870 0,840 Z"/>
      <path class="label-paper" fill="#eef1f0"
            d="M0,205 Q250,30 500,185 L500,575 Q340,820 0,800 Z"/>
    </svg>

    <h1 class="brand-name">ZORIVEN</h1>

    <div class="brand-divider">
      <span class="rule rule--left"></span>
      <span class="flourish" role="img" aria-label="Small decorative ornament"></span>
      <span class="rule rule--right"></span>
    </div>

    <div class="wine-details">
      <p class="grape">Cabernet sauvignon</p>
      <p class="vintage">2010</p>
      <p class="origin">WINE OF CHILE</p>
    </div>

    <div class="art-area" role="img" aria-label="Brand illustration in soft red tones"></div>
  </main>
</body>
</html>
```